HR services to some of biggest Silicon Valley Tech companies needs a new website

We need a new website design probably 4-5 pages initially. Here are some websites we like the look of https://quillmarkgroup.example/ , https://www.vantrel.example/ and https://pemvio.example/ .

Target Market(s)

Silicon valley tech companies

Industry/Entity Type

HR

Coding

Coded - Design and coding required

Number of Pages Required

5+ page

Requirements
Nice to have
• any stock photos or images should show a diverse group of people. Our client base is very diverse

```html
<!DOCTYPE html>
<html lang="en">
<head>
<meta charset="utf-8">
<title>Kestrel HR Consulting</title>
<link href="https://fonts.googleapis.com/css2?family=Montserrat:ital,wght@0,400;0,500;0,600;1,500&family=Raleway:wght@200;300&display=swap" rel="stylesheet">
<style>
:root{
  --gold:#f5b800;
  --gold-band:#e2b000;
  --ink:#222;
  --text:#555;
  --muted:#666;
  --light:#f7f7f7;
  --slate:#5f5f5f;
  --dark:#1b1b1b;
  --white:#fff;
}
*{margin:0;padding:0;box-sizing:border-box}
html,body{width:1200px;height:4386px;overflow:hidden}
body{font-family:"Montserrat",sans-serif;color:var(--text);background:var(--white);position:relative}
section,header,footer{position:absolute;left:0;width:1200px}
.abs{position:absolute}
.thin{font-family:"Raleway",sans-serif;font-weight:200;text-transform:uppercase;letter-spacing:1px}
.btn{position:absolute;background:var(--gold);color:var(--white);font-weight:600;font-size:17px;display:flex;align-items:center;justify-content:center;letter-spacing:.5px}
.wordmark{color:var(--white);font-weight:500;letter-spacing:3px;text-align:center;line-height:1.15}

/* hero */
.hero{top:0;height:732px;background:linear-gradient(100deg,#4b4b4b 0%,#7a7773 45%,#5d5a56 70%,#2f3133 100%)}
.hero .photo{position:absolute;inset:0;background:radial-gradient(ellipse at 70% 30%,rgba(210,200,190,.35),transparent 55%)}
.hero .shade{position:absolute;inset:0;background:linear-gradient(90deg,rgba(0,0,0,.35),rgba(0,0,0,.05) 60%)}
.topmail{top:16px;right:111px;color:var(--white);font-size:17px;display:flex;gap:9px;align-items:center}
.nav{top:62px;right:111px;display:flex;gap:29px;font-size:18px;color:var(--white)}
.nav .on{color:var(--gold)}
.hero-logo{top:60px;left:111px;font-size:30px}
.hero-title{top:342px;left:111px;color:var(--white);font-size:60px;line-height:64px}
.hero .btn{top:499px;left:111px;width:350px;height:63px}

/* welcome */
.welcome{top:732px;height:596px}
.h-big{font-size:54px;color:#333}
.h-sub{font-size:30px;color:var(--gold)}
.welcome p{font-size:15.5px;line-height:26px;color:var(--muted)}
.video{top:82px;left:630px;width:459px;height:304px;background:linear-gradient(135deg,#5a6a78,#9a8a6e 50%,#3e4a56)}
.play{position:absolute;left:205px;top:128px;width:50px;height:50px;border-radius:50%;background:#111}

/* services */
.services{top:1328px;height:614px;background:var(--light)}
.col{position:absolute;top:0;height:614px;padding-top:50px}
.col.dark{background:var(--slate);color:var(--white)}
.col h3{font-weight:500;font-size:22px;line-height:26px;color:#333;height:80px;display:flex;align-items:flex-end}
.col.dark h3{color:var(--white)}
.col ul{list-style:none;margin-top:40px}
.col li{position:relative;padding-left:23px;font-size:15px;line-height:20px;margin-bottom:21px;color:var(--muted)}
.col.dark li{color:#f1f1f1}
.col li::before{content:"";position:absolute;left:0;top:4px;width:12px;height:12px;border-radius:50%;background:var(--gold)}
.col svg{display:block}

/* why */
.why{top:1942px;height:640px}
.feat{position:absolute;width:220px}
.feat h4{font-weight:600;font-size:22px;line-height:26px;color:#333;margin-top:10px}
.why .pic{top:216px;left:660px;width:429px;height:330px;background:linear-gradient(135deg,#3d4a60,#a4b3c4 50%,#4a4038)}

/* testimonial */
.quote{top:2582px;height:482px;background:var(--gold-band)}
.quote blockquote{position:absolute;top:160px;left:220px;width:760px;text-align:center;color:var(--white);font-style:italic;font-weight:500;font-size:24.5px;line-height:38px}
.arrow{position:absolute}

/* team */
.team{top:3064px;height:616px}
.member{position:absolute;top:221px;width:232px;text-align:center}
.member .ph{height:252px;background:linear-gradient(180deg,#d8d8d8,#9d9d9d)}
.member b{display:block;font-weight:600;font-size:22px;color:#333;margin-top:18px}
.member span{display:block;font-size:17px;color:var(--muted);margin-top:4px}

/* cta */
.cta{top:3680px;height:313px;background:linear-gradient(180deg,#8a8a8a,#5b5b5b 60%,#444)}
.cta h2{position:absolute;top:80px;width:1200px;text-align:center;color:var(--white);font-weight:500;font-size:38px;line-height:54px}
.cta .mail{position:absolute;top:200px;width:1200px;display:flex;justify-content:center;gap:10px;align-items:center;color:var(--white);font-size:29px}

/* footer */
.footer{top:3993px;height:393px;background:var(--dark);color:#ddd}
.footer h5{font-weight:600;font-size:17px;color:var(--white)}
.footer .links{list-style:none;font-size:15.5px;line-height:26.6px;margin-top:14px}
.contact-row{display:flex;gap:10px;font-size:15.5px;line-height:26px;margin-top:14px}
.rule{top:296px;left:111px;width:978px;height:1px;background:#3a3a3a}
.social{top:326px;width:42px;height:42px;border:1.5px solid #ccc;border-radius:50%}
</style>
</head>
<body>

<header class="hero">
  <div class="photo" role="img" aria-label="Photo of a diverse team of colleagues smiling in a meeting"></div>
  <div class="shade"></div>
  <div class="abs topmail">
    <svg width="17" height="13" viewBox="0 0 17 13"><rect width="17" height="13" rx="1.5" fill="#f5b800"/><path d="M1 1.5l7.5 6 7.5-6" stroke="#fff" stroke-width="1.4" fill="none"/></svg>
    info@kestrelhr.example
  </div>
  <nav class="abs nav"><span class="on">Home</span><span>About us</span><span>Services</span><span>Team</span><span>Blog</span><span>Contact Us</span></nav>
  <div class="abs wordmark hero-logo">KESTREL HR<br>CONSULTING</div>
  <h1 class="abs thin hero-title">Our team<br>supports yours</h1>
  <div class="btn">REQUEST A FREE CONSULTATION</div>
</header>

<section class="welcome">
  <h2 class="abs thin h-big" style="top:70px;left:111px">Welcome to</h2>
  <div class="abs thin h-sub" style="top:136px;left:111px">Kestrel HR Consulting</div>
  <div class="abs" style="top:196px;left:111px;width:470px">
    <p>Kestrel HR Consulting is the solution to all your HR issues. We are a one-stop-shop providing a variety of services</p>
    <p style="margin-top:25px">Whether you have a specific HR need or seek relief by outsourcing altogether, we have you covered</p>
    <p style="margin-top:25px">For some clients, a Kestrel Consultant is known as the HR department and for others, we simply step in as needed on a project basis</p>
  </div>
  <div class="btn" style="top:465px;left:111px;width:156px;height:51px">READ MORE</div>
  <div class="abs video" role="img" aria-label="Video still of a diverse team working around laptops">
    <div class="play"><svg width="50" height="50"><path d="M20 15l15 10-15 10z" fill="#fff"/></svg></div>
  </div>
</section>

<section class="services">
  <div class="col" style="left:0;width:301px;padding-left:31px;padding-right:14px">
    <svg width="74" height="74" viewBox="0 0 74 74" fill="none" stroke="#333" stroke-width="2"><rect x="3" y="4" width="46" height="64"/><path d="M12 18h28M12 28h28M12 38h18M12 48h18"/><circle cx="52" cy="42" r="11" stroke="#f5b800"/><circle cx="52" cy="42" r="4" stroke="#f5b800"/></svg>
    <h3>Setup</h3>
    <ul><li>Select and implement an HRIS system</li><li>Create Company Handbook</li><li>Write termination procedure</li><li>Set up benefits services</li><li>Set up workers comp vendor</li><li>Create job descriptions for current and anticipated roles</li></ul>
  </div>
  <div class="col dark" style="left:301px;width:298px;padding-left:22px;padding-right:14px">
    <svg width="80" height="80" viewBox="0 0 80 80" fill="none" stroke-width="2"><path d="M12 40a28 28 0 0 1 48-20" stroke="#f5b800"/><path d="M68 40a28 28 0 0 1-48 20" stroke="#f5b800"/><rect x="26" y="24" width="22" height="30" stroke="#fff"/><rect x="32" y="30" width="22" height="30" stroke="#fff"/></svg>
    <h3>Recurring<br>Procedures</h3>
    <ul><li>Review handbook annually</li><li>Roll out training (required and soft skills training)</li><li>Write offer letters</li><li>Handle employee data and files</li><li>Conduct I-9 audits</li><li>Handle merit and review bonuses</li></ul>
  </div>
  <div class="col" style="left:599px;width:320px;padding-left:43px">
    <svg width="94" height="90" viewBox="0 0 94 90" fill="none" stroke-width="2"><path d="M10 45a37 37 0 0 1 70-18" stroke="#f5b800"/><path d="M84 45a37 37 0 0 1-70 18" stroke="#f5b800"/><circle cx="47" cy="36" r="8" stroke="#333"/><path d="M32 60c0-10 30-10 30 0" stroke="#333"/></svg>
    <h3>Managing<br>HR Functions</h3>
    <ul><li>Onboarding/Offboarding</li><li>Employee relations</li><li>Investigations</li><li>Leave administration</li><li>Immigration liaison</li><li>Compensation management</li><li>Full cycle recruitment</li></ul>
  </div>
  <div class="col" style="left:919px;width:281px;padding-left:0;padding-right:12px">
    <svg width="90" height="80" viewBox="0 0 90 80" fill="none" stroke-width="2"><rect x="30" y="2" width="40" height="52" stroke="#333"/><path d="M38 14h24M38 24h24" stroke="#333"/><path d="M8 72l30-30M20 76l34-34" stroke="#f5b800"/><circle cx="66" cy="46" r="7" stroke="#f5b800"/></svg>
    <h3>Partner<br>Communications<br>&amp; Projects</h3>
    <ul><li>Manage annual bidding process for benefits review</li><li>Handle workers compensation claims administration</li><li>Manage leave administration between client, employee and vendor(s)</li><li>Handle EDD inquires</li><li>Partner on M&amp;A activity</li></ul>
  </div>
</section>

<section class="why">
  <div class="feat" style="top:80px;left:111px">
    <svg width="72" height="72" viewBox="0 0 72 72" fill="none" stroke="#333" stroke-width="2"><circle cx="36" cy="6" r="4"/><circle cx="14" cy="18" r="4"/><circle cx="58" cy="18" r="4"/><circle cx="10" cy="42" r="4"/><circle cx="62" cy="42" r="4"/><circle cx="36" cy="64" r="4"/><path d="M32 26v16h10v-10" stroke="#f5b800"/></svg>
    <h4>One-stop-shop</h4>
  </div>
  <div class="feat" style="top:75px;left:364px">
    <svg width="72" height="72" viewBox="0 0 72 72" fill="none" stroke="#333" stroke-width="2"><circle cx="12" cy="8" r="5"/><circle cx="36" cy="8" r="5"/><circle cx="60" cy="8" r="5"/><circle cx="36" cy="48" r="16" stroke="#f5b800"/><circle cx="36" cy="44" r="5" stroke="#f5b800"/></svg>
    <h4>Outsourcing<br>altogether</h4>
  </div>
  <div class="feat" style="top:246px;left:111px">
    <svg width="72" height="72" viewBox="0 0 72 72" fill="none" stroke="#333" stroke-width="2"><circle cx="18" cy="22" r="8"/><circle cx="54" cy="22" r="8"/><circle cx="36" cy="30" r="9" stroke="#f5b800"/><path d="M4 62c0-18 28-18 28 0M40 62c0-18 28-18 28 0"/></svg>
    <h4>Experienced<br>Professionals</h4>
  </div>
  <div class="feat" style="top:246px;left:364px">
    <svg width="72" height="72" viewBox="0 0 72 72" fill="none" stroke="#333" stroke-width="2"><path d="M24 48a20 20 0 1 1 24 0v8H24z"/><path d="M28 64h16"/><circle cx="36" cy="28" r="8" stroke="#f5b800"/></svg>
    <h4>Innovative<br>Strategies</h4>
  </div>
  <div class="feat" style="top:425px;left:111px">
    <svg width="72" height="64" viewBox="0 0 72 64" fill="none" stroke="#333" stroke-width="2"><path d="M10 60V24a20 20 0 0 1 40 0l6 14h-8v14H34v8"/><rect x="12" y="20" width="22" height="16" stroke="#f5b800"/></svg>
    <h4>Partnership<br>Mentality</h4>
  </div>
  <div class="feat" style="top:425px;left:364px">
    <svg width="72" height="72" viewBox="0 0 72 72" fill="none" stroke="#333" stroke-width="2"><circle cx="36" cy="36" r="32" stroke-dasharray="10 4"/><path d="M24 48V32h8l6-12 4 2-2 10h10l-2 16z" stroke="#f5b800"/></svg>
    <h4>Maintain Best<br>Practices</h4>
  </div>
  <h2 class="abs thin h-big" style="top:80px;left:657px">Why choose</h2>
  <div class="abs thin h-sub" style="top:143px;left:657px">Kestrel HR Consulting</div>
  <div class="abs pic" role="img" aria-label="Photo of three diverse colleagues reviewing work on a laptop"></div>
</section>

<section class="quote">
  <svg class="arrow" style="top:224px;left:53px" width="20" height="34" viewBox="0 0 20 34"><path d="M17 2L3 17l14 15" stroke="#fff" stroke-width="3" fill="none"/></svg>
  <svg class="arrow" style="top:224px;left:1120px" width="20" height="34" viewBox="0 0 20 34"><path d="M3 2l14 15L3 32" stroke="#fff" stroke-width="3" fill="none"/></svg>
  <svg class="abs" style="top:72px;left:570px" width="60" height="48" viewBox="0 0 60 48"><path d="M4 46V26C4 12 12 4 24 2v8c-7 2-10 7-10 14h10v22zM34 46V26C34 12 42 4 54 2v8c-7 2-10 7-10 14h10v22z" fill="#fff"/></svg>
  <blockquote>“ Nemo enim ipsam voluptatem quia voluptas sit asper natur aut odit aut fugit, sed quia consequuntur magni dolo res eos qui ratione voluptatem sequi nesci unt. Neque porro quisquam est, qui dolorem ipsum quiad.”</blockquote>
  <svg class="abs" style="top:308px;left:560px" width="80" height="80" viewBox="0 0 80 80"><circle cx="40" cy="40" r="40" fill="#fff"/><circle cx="40" cy="32" r="12" fill="#ddd"/><path d="M16 66c4-16 44-16 48 0" fill="#ddd"/></svg>
  <div class="abs" style="top:400px;width:1200px;text-align:center;color:#fff;font-size:22px;font-weight:500">Ines</div>
</section>

<section class="team">
  <h2 class="abs thin h-big" style="top:78px;width:1200px;text-align:center">Our team</h2>
  <div class="abs thin h-sub" style="top:140px;width:1200px;text-align:center">Meet the people</div>
  <svg class="arrow" style="top:330px;left:53px" width="20" height="34" viewBox="0 0 20 34"><path d="M17 2L3 17l14 15" stroke="#777" stroke-width="3" fill="none"/></svg>
  <svg class="arrow" style="top:330px;left:1120px" width="20" height="34" viewBox="0 0 20 34"><path d="M3 2l14 15L3 32" stroke="#777" stroke-width="3" fill="none"/></svg>
  <div class="member" style="left:111px"><div class="ph" role="img" aria-label="Portrait of the CEO"></div><b>Maren Okafor</b><span>CEO</span></div>
  <div class="member" style="left:359px"><div class="ph" role="img" aria-label="Portrait of a manager"></div><b>Dario</b><span>Manager</span></div>
  <div class="member" style="left:608px"><div class="ph" role="img" aria-label="Portrait of a manager"></div><b>Leila</b><span>Manager</span></div>
  <div class="member" style="left:856px"><div class="ph" role="img" aria-label="Portrait of a manager"></div><b>Tomas</b><span>Manager</span></div>
</section>

<section class="cta" role="img" aria-label="Muted photo of a city skyline behind the call to action">
  <h2>We look forward to working with you<br>Contact us for a free consultation</h2>
  <div class="mail">
    <svg width="28" height="21" viewBox="0 0 17 13"><rect width="17" height="13" rx="1.5" fill="#f5b800"/><path d="M1 1.5l7.5 6 7.5-6" stroke="#666" stroke-width="1.4" fill="none"/></svg>
    info@kestrelhr.example
  </div>
</section>

<footer class="footer">
  <div class="abs wordmark" style="top:90px;left:108px;font-size:34px;width:285px">KESTREL HR<br>CONSULTING</div>
  <div class="abs" style="top:58px;left:517px">
    <h5>Quick Links</h5>
    <ul class="links"><li>Home</li><li>About us</li><li>Services</li><li>Team</li><li>Blog</li><li>Contact Us</li></ul>
  </div>
  <div class="abs" style="top:58px;left:749px">
    <h5>Contact Us</h5>
    <div class="contact-row"><svg width="10" height="16" viewBox="0 0 10 16" style="margin-top:4px"><path d="M5 0a5 5 0 0 1 5 5c0 4-5 11-5 11S0 9 0 5a5 5 0 0 1 5-5z" fill="#f5b800"/><circle cx="5" cy="5" r="2" fill="#1b1b1b"/></svg><span>No 12300 enim ad minieniam,<br>quis nostrum exercita</span></div>
    <div class="contact-row" style="margin-top:22px"><svg width="14" height="14" viewBox="0 0 14 14" style="margin-top:6px"><path d="M3 1l3 3-2 2c1 2 2 3 4 4l2-2 3 3-2 2C6 13 1 8 1 3z" fill="#f5b800"/></svg><span>1 555 010 0199</span></div>
    <div class="contact-row" style="margin-top:26px"><svg width="15" height="11" viewBox="0 0 17 13" style="margin-top:8px"><rect width="17" height="13" rx="1.5" fill="#f5b800"/><path d="M1 1.5l7.5 6 7.5-6" stroke="#1b1b1b" stroke-width="1.4" fill="none"/></svg><span>info@kestrelhr.example</span></div>
  </div>
  <div class="abs rule"></div>
  <div class="abs" style="top:337px;left:111px;font-size:15.5px">© 2021 Kestrel HR Consulting . All Rights Reserved.</div>
  <div class="abs social" style="left:945px"></div>
  <div class="abs social" style="left:994px"></div>
  <div class="abs social" style="left:1043px"></div>
</footer>

</body>
</html>
```